Candle company needs a label for candle

Looking for a designer to create my candle label. I am going to attach a few pictures of my vision for the label as well as my Company Logo and jar I have puchased. I'm going for the modern rustic feel but you are the designer and have full trust in your abilities. The label is going to be printed on Kraft paper (2x3) so looking for the font to be black. The candle label MUST include the following information:
Candle Birchway Co.
NO. 01: Eucalyptus + Spearmint
Handmade In NJ
Soy Wax
9oz

Industry/Entity Type

Candle Industry

Colors

Designer to choose colors to be used in the design.

Requirements
Should not have
• Any images

```html
<!DOCTYPE html>
<html lang="en">
<head>
<meta charset="UTF-8">
<title>Candle Birchway Co. — No. 01 Label</title>
<link rel="stylesheet" href="https://fonts.googleapis.com/css2?family=EB+Garamond:wght@400;700&display=swap">
<style>
  :root {
    --page: #ffffff;
    --kraft: #c59b6c;
    --kraft-light: #cfa676;
    --kraft-dark: #bb9162;
    --ink: #1c1c1a;
  }
  html, body {
    margin: 0;
    padding: 0;
    width: 1200px;
    height: 1200px;
    overflow: hidden;
    background: var(--page);
  }
  .canvas {
    position: relative;
    width: 1200px;
    height: 1200px;
  }
  .label {
    position: absolute;
    left: 118px;
    top: 279px;
    width: 965px;
    height: 642px;
    background:
      radial-gradient(ellipse at 30% 60%, var(--kraft-light) 0%, transparent 60%),
      radial-gradient(ellipse at 80% 20%, var(--kraft-dark) 0%, transparent 55%),
      var(--kraft);
    color: var(--ink);
    font-family: "EB Garamond", Garamond, serif;
  }
  .brand-name {
    position: absolute;
    left: 0;
    right: 0;
    top: 180px;
    margin: 0;
    text-align: center;
    font-weight: 400;
    font-size: 62px;
    line-height: 1;
    letter-spacing: 0.06em;
  }
  .scent-title {
    position: absolute;
    left: 0;
    right: 0;
    top: 420px;
    margin: 0;
    text-align: center;
    font-weight: 700;
    font-size: 56px;
    line-height: 1;
  }
  .details {
    position: absolute;
    left: 71px;
    top: 504px;
    width: 822px;
    height: 92px;
    border-top: 2px solid var(--ink);
    display: grid;
    grid-template-columns: 235px 425px 162px;
    font-size: 44px;
  }
  .details span {
    display: flex;
    align-items: center;
    justify-content: center;
    padding-bottom: 14px;
  }
  .details .divided {
    border-left: 2px solid var(--ink);
    border-right: 2px solid var(--ink);
  }
</style>
</head>
<body>
  <div class="canvas">
    <section class="label">
      <h1 class="brand-name">Candle Birchway Co.</h1>
      <h2 class="scent-title">NO. 01: Eucalyptus + Spearmint</h2>
      <div class="details">
        <span>Soy Wax</span>
        <span class="divided">Handmade In NJ</span>
        <span>9oz</span>
      </div>
    </section>
  </div>
</body>
</html>
```